Etiketten-Design für Nahrungsergänzungsmittel
Zielgruppe
Die Firma vertreibt Nahrungsergänzungsmittel, gesunde Lebensmittel, Lifestyle und Wellnessprodukte. Dies vor allem im Fitness und Sport Bereich. Die Marke und das entsprechende Logo sollen auf eine jüngere Zielgruppe 25+ ausgerichtet sein. Personen die für Ihren Körper und Gesundheit Sport treiben und zusätzlich Unterstützung benötigen. Die Produkte werden über Pictoloop durch eine Fitnesstrainerin beworben, und hauptsächlich über Varuno vertrieben. Produkte sind z. B. Produkte zur Ausdauersteigerung, verbesserte Konzentration, Schlaf, Stressbewältigung. Protein Shakes oder Vitamine für Veganer. No gos, Diät Produkte 5kg in 3 Tagen, Potenzsteigerung, Brustvergrößerung oder ähnliches.
Aufgabenstellung
Das Etikett wird auf einen wiederverschließbaren schwarz matten Kraftpapier Beutel im Format 28x20cm aufgebracht. Der Beutel und auch das Etikett sind kompostierbar, sieht aber beides hochwertig aus. Das Produkt ist ein veganes Proteinpulver zum anrühren mit Wasser oder Milchalternative. Einen ersten Entwurf habe ich hochgeladen.

```html
<!DOCTYPE html>
<html lang="de">
<head>
<meta charset="utf-8">
<title>ELVARA Plant Power 7X – Etikett</title>
<link href="https://fonts.googleapis.com/css2?family=Barlow+Condensed:ital,wght@1,700;1,800&family=Outfit:wght@400;600;700;800&display=swap" rel="stylesheet">
<style>
  :root{
    --stage:#282828;
    --panel-dark:#1c1c1c;
    --panel-mid:#252525;
    --teal:#00a19a;
    --white:#ffffff;
    --rule:#9a9a9a;
  }
  *{box-sizing:border-box;margin:0;padding:0}
  html,body{width:1200px;height:1200px;overflow:hidden;background:var(--stage)}
  body{position:relative;font-family:"Outfit",sans-serif;color:var(--white)}
  .label{position:absolute;top:247px;width:511px;height:716px;border:3px solid var(--white);border-radius:28px;overflow:hidden;background:var(--panel-mid)}
  .label--front{left:65px}
  .label--back{left:624px}
  .label__bg{position:absolute;left:0;top:0;width:100%;height:100%}

  /* front */
  .brand{position:absolute;left:0;width:100%;top:190px;text-align:center;font-family:"Outfit",sans-serif;font-weight:800;font-size:52px;letter-spacing:1px;color:var(--white)}
  .title{position:absolute;left:0;width:100%;text-align:center;font-family:"Barlow Condensed",sans-serif;font-style:italic;font-weight:800;line-height:1}
  .title--line1{top:424px;font-size:56px;color:var(--teal)}
  .title--line2{top:477px;font-size:58px;color:var(--white)}
  .subtitle{position:absolute;top:531px;left:0;width:100%;display:flex;align-items:center;justify-content:center;gap:8px;font-family:"Barlow Condensed",sans-serif;font-style:italic;font-weight:700;font-size:22px;color:var(--teal)}
  .subtitle__line{display:block;width:48px;height:2px;background:var(--white)}
  .flavour{position:absolute;right:63px;top:651px;text-align:right;font-family:"Barlow Condensed",sans-serif;font-style:italic;color:var(--white);line-height:1}
  .flavour__name{font-weight:700;font-size:21px}
  .flavour__weight{font-family:"Outfit",sans-serif;font-weight:400;font-size:13px;margin-top:2px}
  .brand-dot{position:absolute;left:453px;top:655px;width:34px;height:34px;border-radius:50%;border:2px solid var(--panel-dark)}

  /* back */
  .back-text{position:absolute;left:53px;font-size:10px;line-height:13px}
  .product-desc{top:49px;width:410px;font-weight:700;font-size:10.5px;line-height:14px;white-space:nowrap}
  .ingredients{top:88px;width:400px;line-height:13px}
  .table{position:absolute;left:53px;width:401px;border-collapse:collapse;font-size:9.5px;text-align:center}
  .table th,.table td{border-bottom:1px solid var(--rule);padding:0 2px;font-weight:400}
  .table th{font-weight:700}
  .table td+td,.table th+th{border-left:1px solid var(--rule)}
  .table--nutrition{top:136px;border-top:1px solid var(--rule)}
  .table--nutrition tr{height:18px}
  .table--nutrition tr.row-energy{height:36px}
  .table--nutrition td{line-height:12px}
  .table--amino{top:328px;border-top:1px solid var(--rule)}
  .table--amino tr{height:18px}
  .table--amino thead th{border-left:none}
  .usage{top:494px;font-size:10.5px;line-height:14px;white-space:nowrap}
  .usage p+p{margin-top:4px}
  .usage strong{font-weight:700}
  .photo{position:absolute;left:345px;top:476px;width:155px;height:240px;border-radius:60px 60px 0 0;background:linear-gradient(180deg,#3c4a50 0%,#4a7583 45%,#1d1d1d 100%)}
  .social{position:absolute;right:174px;top:664px;text-align:right;font-weight:700;font-size:7.5px;line-height:8.5px}
  .social__handle{display:flex;align-items:center;justify-content:flex-end;gap:2px;font-size:10.5px;line-height:13px;margin-top:1px}
  .social__dot{width:7px;height:7px;border-radius:50%;border:1px solid var(--white)}
</style>
</head>
<body>

<section class="label label--front" aria-label="Etikett Vorderseite">
  <svg class="label__bg" viewBox="0 0 511 716" preserveAspectRatio="none" aria-hidden="true">
    <polygon points="0,0 511,0 511,300 0,396" fill="var(--panel-dark)"/>
    <polygon points="0,0 217,0 0,43" fill="var(--teal)"/>
    <polygon points="338,333 511,300 511,313" fill="var(--teal)"/>
    <polygon points="0,675 171,654 0,687" fill="var(--teal)"/>
    <polygon points="0,700 511,605 511,716 0,716" fill="var(--teal)"/>
  </svg>
  <div class="brand">ELVARA</div>
  <div class="title title--line1">PLANT</div>
  <div class="title title--line2">POWER 7X</div>
  <div class="subtitle"><span class="subtitle__line"></span>Samen Kerne Blend<span class="subtitle__line"></span></div>
  <div class="flavour">
    <div class="flavour__name">Vanille, reis, Erbse</div>
    <div class="flavour__weight">600g</div>
  </div>
  <span class="brand-dot" aria-hidden="true"></span>
</section>

<section class="label label--back" aria-label="Etikett Rückseite">
  <svg class="label__bg" viewBox="0 0 511 716" preserveAspectRatio="none" aria-hidden="true">
    <polygon points="0,0 511,0 511,300 0,396" fill="var(--panel-dark)"/>
    <polygon points="0,700 511,605 511,716 0,716" fill="var(--teal)"/>
  </svg>

  <p class="back-text product-desc">Getränkepulver zur Herstellung eines veganen Eiweißgetränkes mit<br>Süßungsmittel - Geschmacksrichtung Vanille</p>
  <p class="back-text ingredients">Zutaten: Eiweißmischung (93%) (Erbseneiweiß, Reiseiweiß, Hanfsamenpulver, Bio Kürbiskerneiweiß), Aroma, Verdckungsmittel: Xanthan, Kokosnussmilchpulver, Süßungsmittel: Sucralose</p>

  <table class="table table--nutrition">
    <colgroup><col style="width:174px"><col style="width:122px"><col style="width:105px"></colgroup>
    <tr><th>Nahrwertangaben pro</th><th>100g</th><th>Portion = 30g</th></tr>
    <tr class="row-energy"><td>Energie</td><td>1.694 kJ /<br>401 kcal</td><td>508 kJ /<br>120 kcal</td></tr>
    <tr><td>Fett</td><td>8,3 g</td><td>2,5 g</td></tr>
    <tr><td>- davon gesättigte Fettsäuren</td><td>2,2 g</td><td>0,7 g</td></tr>
    <tr><td>Kohlenhydrate</td><td>4,0 g</td><td>1,2 g</td></tr>
    <tr><td>- davon Zucker</td><td>1,2 g</td><td>0,4 g</td></tr>
    <tr><td>Bllaststoffe</td><td>4,4 g</td><td>1,3 g</td></tr>
    <tr><td>Eiweiß</td><td>75,3 g</td><td>22,6 g</td></tr>
    <tr><td>Salz</td><td>2, 15 g</td><td>0,64 g</td></tr>
  </table>

  <table class="table table--amino">
    <colgroup><col style="width:85px"><col style="width:60px"><col style="width:87px"><col style="width:43px"><col style="width:79px"><col style="width:47px"></colgroup>
    <thead><tr><th colspan="6">Aminosäurenprofil pro 100g Eweiß</th></tr></thead>
    <tbody>
      <tr><td>Isoleucin</td><td>4,4 g</td><td>Tryptophan</td><td>1,1 g</td><td>Alanin</td><td>8,9 g</td></tr>
      <tr><td>Leucin</td><td>8,4 g</td><td>Valin</td><td>5,3 g</td><td>Asparaginsäure</td><td>11,1 g</td></tr>
      <tr><td>Lysin</td><td>6,7 g</td><td>Histidin</td><td>2,5 g</td><td>Glutaminsäure</td><td>17,2 g</td></tr>
      <tr><td>Methionin</td><td>1,4 g</td><td>Arginin</td><td>8,9 g</td><td>Glycin</td><td>4,2 g</td></tr>
      <tr><td>Phenylalanin</td><td>5,5 g</td><td>Tyrosin</td><td>3,8 g</td><td>Prolin</td><td>4,4 g</td></tr>
      <tr><td>Threonin</td><td>3,7 g</td><td>Cystein</td><td>1,4 g</td><td>Serin</td><td>5,1 g</td></tr>
    </tbody>
  </table>

  <div class="back-text usage">
    <p><strong>Verzehrempfehlung:</strong> 30 g Pulver<br><strong>in 300 ml Wasser lösen;</strong><br>Das Produkt ist kuhl, trocken und<br>dunkel zu lagern.</p>
    <p><strong>ELVAUG</strong><br>Lindenhofweg 12<br>71234 Wiesental<br>info@elvarabyelva.de</p>
    <p>Inhalt: 600g Eiweipulver fur 20 Shakes<br>Mindestens halbar bis Ende:<br>08/2023; Losnummer: 977109</p>
  </div>

  <div class="photo" role="img" aria-label="Foto der Fitnesstrainerin in Sportkleidung"></div>

  <div class="social">
    Besucht uns<br>auch auf Pictoloop<br>Liebe Grüße Elva
    <div class="social__handle"><span class="social__dot"></span>elvarabyelva</div>
  </div>
</section>

</body>
</html>
```